my website is tabellepiece.com. (brand name is ta belle pièce) This is just a template that i have choose for. The content and the pictures are not about my business just the template.
I would like to have 4 pages for now. 1 homepage, which will be an overview for all pages, it is right now in this way. It will directly highlight my story. My website will tell an exclusive story about details which makes the difference and will make people happy with very small things. It will be art related but very stylish as well. I also want to have a event agenda on my homepage where people can see where my next event is. Page 2 my blog, where I will write weekly about mindset, lifestyle and details. Inspiration place for people who are looking for unique and exclusive approaches in life. Page 3 shop, where I will sell my stuff which is handmade and unique, it will be limited edition stuff. Mostly I will make the designs from marbling art, which I am a teacher for. (https://www.vidorastream.com/watch?v=Kq7TbWm2Xa) check this video out for more. Page 4 is book page. Here people will be able to book private or group classes for marbling art (check the video). I have already a community of more than 500 people on join ring, which will be my public as well. I wanna implement the join ring button on this page as well. to be able to track.

This is about my website. I also need a logo for my brand, which will suit my website and my goals.

I can also give you a reference website, which really like as structure and style;
https://www.brightmorrowco.com/products/the-daybook-organizer?ref=Xp4RtLm8QzVw2NbKc7HsJd9FgTy3MvEqBa6WnUoZr1LkPxYhGiCe5DsAtQfVbNj0HmRwKyXo8LcTpZaEsUv2GqDnIwMb

ta belle pièce

4 page

• I can also give you a reference website, which really like as structure and style;
• https://www.brightmorrowco.com/products/the-daybook-organizer?ref=Xp4RtLm8QzVw2NbKc7HsJd9FgTy3MvEqBa6WnUoZr1LkPxYhGiCe5DsAtQfVbNj0HmRwKyXo8LcTpZaEsUv2GqDnIwMb

```html
<!DOCTYPE html>
<html lang="en">
<head>
<meta charset="utf-8">
<title>ta belle pièce — Home</title>
<link href="https://fonts.googleapis.com/css2?family=Poppins:wght@400;500;600;700&family=Open+Sans:wght@400;600&display=swap" rel="stylesheet">
<style>
:root{
  --pink:#eeaacb;
  --pink-soft:#dea6c4;
  --pink-deep:#e58fb8;
  --ink:#222222;
  --text:#555555;
  --muted:#8a8a8a;
  --grey-bg:#f4f4f4;
  --grey-seg:#9a9a9a;
  --white:#ffffff;
  --black:#000000;
  --line:#e2e2e2;
}
*{box-sizing:border-box;margin:0;padding:0}
html,body{width:1200px;height:3297px;overflow:hidden}
body{font-family:"Open Sans",Arial,sans-serif;color:var(--text);background:var(--white);position:relative}
.abs{position:absolute}
h1,h2,h3,h4,.nav,.btn{font-family:"Poppins",Arial,sans-serif}

/* header */
.site-header{position:absolute;top:0;left:0;width:1200px;height:105px;background:var(--white)}
.nav a{position:absolute;top:43px;font-size:16px;color:#333;text-decoration:none}
.nav a.active{color:var(--ink);font-weight:500}
.nav .sep{position:absolute;top:38px;width:1px;height:30px;background:var(--line)}
.brand{position:absolute;top:36px;left:505px;width:190px;text-align:center;font-family:"Poppins",sans-serif;font-weight:600;font-size:22px;color:var(--ink);letter-spacing:.5px}
.cart{position:absolute;left:1029px;top:42px;width:24px;height:24px;border-radius:50%;background:var(--pink)}
.search{position:absolute;left:1084px;top:46px}

/* hero */
.hero{position:absolute;top:105px;left:0;width:1200px;height:576px}
.hero-art{position:absolute;inset:0;background:
 radial-gradient(ellipse at 25% 70%,#6f4b78 0%,transparent 45%),
 radial-gradient(ellipse at 75% 65%,#7c5684 0%,transparent 45%),
 radial-gradient(ellipse at 55% 20%,#8a6b4a 0%,transparent 40%),
 linear-gradient(135deg,#5a4a3e 0%,#8e7a8f 40%,#6e5a76 70%,#4e4456 100%)}
.hero-shade{position:absolute;inset:0;background:rgba(0,0,0,.25)}
.hero h1{position:absolute;top:172px;left:0;width:1200px;text-align:center;color:var(--white);font-size:42px;font-weight:600;line-height:46px;letter-spacing:.5px}
.hero p{position:absolute;top:284px;left:370px;width:460px;text-align:center;color:var(--white);font-size:12.5px;line-height:22px}
.btn{display:inline-block;text-decoration:none;font-weight:600;font-size:13px;text-transform:uppercase}
.hero .btn{position:absolute;top:387px;left:530px;width:140px;height:34px;line-height:34px;text-align:center;border-radius:17px;background:var(--white);color:var(--ink)}
.hero .arrow{position:absolute;top:278px;color:var(--white);font-size:22px}

/* about */
.about{position:absolute;top:681px;left:0;width:1200px;height:462px}
.about-photo{position:absolute;inset:0;background:linear-gradient(160deg,#3a3b2c 0%,#6b4a3c 35%,#8a5a4a 60%,#5c4a3a 100%)}
.about-panel{position:absolute;inset:0}
.about h2{position:absolute;top:100px;left:99px;font-size:38px;font-weight:600;color:var(--white);letter-spacing:.5px}
.about p{position:absolute;left:99px;width:450px;color:var(--white);font-size:11.5px;line-height:20px}
.about .btn{position:absolute;top:328px;left:99px;width:125px;height:30px;line-height:30px;border-radius:15px;background:var(--white);color:var(--ink);font-size:12px;text-align:center}

/* why */
.why{position:absolute;top:1143px;left:0;width:1200px;height:637px;background:var(--grey-bg)}
.section-title{position:absolute;left:0;width:1200px;text-align:center;font-size:34px;font-weight:500;color:var(--ink);letter-spacing:.5px}
.why .rule{position:absolute;top:130px;left:570px;width:60px;height:2px;background:#555}
.feature{position:absolute;width:240px}
.feature h3{font-size:16px;font-weight:500;color:var(--ink);margin-bottom:8px}
.feature p{font-size:11.5px;line-height:20px;color:var(--text)}
.feature.left{left:92px;text-align:right}
.feature.right{left:877px;text-align:left}

/* shop */
.shop{position:absolute;top:1780px;left:0;width:1200px;height:561px;background:var(--white)}
.shop-photo{position:absolute;left:99px;top:115px;width:400px;height:332px;background:linear-gradient(180deg,#5a3a2e 0%,#8f7a62 30%,#9cb7b8 55%,#7fa39a 100%)}
.price{position:absolute;left:415px;top:115px;width:84px;height:40px;line-height:40px;background:rgba(34,34,34,.85);color:var(--white);font-family:"Poppins",sans-serif;font-size:15px;text-align:center}
.shop h2{position:absolute;left:532px;top:134px;font-size:32px;font-weight:500;color:var(--ink)}
.shop .lead{position:absolute;left:532px;top:193px;width:570px;font-size:11.5px;line-height:21px}
.bullets{position:absolute;left:532px;top:310px;width:570px;font-size:11.5px;line-height:24px;list-style:none;display:grid;grid-template-columns:242px 1fr}
.bullets li{padding-left:18px;position:relative}
.bullets li::before{content:"";position:absolute;left:0;top:7px;width:10px;height:10px;border-radius:50%;background:#333}
.shop .btn{position:absolute;left:532px;top:385px;width:123px;height:32px;line-height:32px;background:var(--pink);color:var(--white);font-size:12.5px;text-align:center;border-radius:2px}

/* events */
.events{position:absolute;top:2341px;left:0;width:1200px;height:543px;background:var(--grey-bg)}
.event{position:absolute;top:149px;width:310px}
.event-photo{height:172px}
.event .date{position:absolute;left:10px;top:-10px;width:66px;height:70px;background:var(--pink);color:var(--white);text-align:center;font-family:"Poppins",sans-serif;line-height:1}
.event .date span{display:block}
.event .m{font-size:10px;padding-top:8px}
.event .d{font-size:26px;font-weight:500;padding-top:3px}
.event .y{font-size:11px;padding-top:3px}
.event h3{font-size:17px;font-weight:400;color:var(--ink);margin-top:17px}
.event .meta{margin-top:12px;font-size:11px;color:var(--muted);display:flex;gap:14px;align-items:center}
.stars{color:#f0b400;letter-spacing:1px;font-size:12px}
.stars .off{color:#ccc}
.event p{margin-top:10px;font-size:11px;line-height:18px}

/* footer */
.site-footer{position:absolute;top:2884px;left:0;width:1200px;height:336px;background:var(--black);color:var(--white)}
.footer-brand{position:absolute;left:100px;top:110px;width:150px;font-family:"Poppins",sans-serif;font-size:22px;font-weight:500;color:var(--white);text-align:center}
.socials{position:absolute;left:116px;top:222px;display:flex;gap:6px}
.socials span{width:20px;height:20px;border:1px solid #777;border-radius:50%}
.site-footer h4{position:absolute;top:70px;font-size:16px;font-weight:500;letter-spacing:.5px}
.contact li{position:absolute;left:295px;list-style:none;font-size:12px;line-height:19px;padding-left:27px}
.contact svg{position:absolute;left:0;top:3px}
.news-text{position:absolute;left:622px;top:106px;width:270px;font-size:11px;line-height:19px}
.news-form{position:absolute;left:622px;top:162px;display:flex}
.news-form .input{width:191px;height:42px;background:var(--white);color:#999;font-size:11px;padding:14px 12px}
.news-form .submit{width:88px;height:42px;line-height:42px;background:var(--pink);color:var(--ink);font-size:12px;text-align:center;font-family:"Poppins",sans-serif}
.cards{position:absolute;left:622px;top:233px;display:flex;gap:6px}
.cards span{width:38px;height:26px;background:var(--white);border-radius:3px}
.links{position:absolute;left:974px;top:107px;list-style:none;font-size:11.5px;line-height:22.6px}
.bottom-bar{position:absolute;top:3220px;left:0;width:1200px;height:77px;background:var(--black);border-top:1px solid #222;color:var(--white);text-align:center;font-size:11px;line-height:77px}
</style>
</head>
<body>

<header class="site-header">
  <nav class="nav">
    <a class="active" style="left:246px">Home</a>
    <span class="sep" style="left:336px"></span>
    <a style="left:375px">My Blog</a>
    <div class="brand">ta belle pièce</div>
    <a style="left:778px">Shop</a>
    <span class="sep" style="left:858px"></span>
    <a style="left:901px">Book</a>
  </nav>
  <span class="cart"></span>
  <svg class="search" width="16" height="16" viewBox="0 0 16 16"><circle cx="6.5" cy="6.5" r="5" fill="none" stroke="#333" stroke-width="2"/><line x1="10.5" y1="10.5" x2="15" y2="15" stroke="#333" stroke-width="2"/></svg>
</header>

<section class="hero">
  <div class="hero-art" role="img" aria-label="Close-up of marbling paint in purple, green and red swirls"></div>
  <div class="hero-shade"></div>
  <span class="arrow" style="left:38px">‹</span>
  <span class="arrow" style="left:1150px">›</span>
  <h1>OUR NEW ARRIVALS<br>ARE HERE</h1>
  <p>ta belle pièce is a leading Online Store. We provide an unparalleled selection of the very best quality products, an easy and comfortable shopping experience, expedited shipping offers, and exceptional customer service. Check out our collection of new arrivals, best-sellers, and clearance items today.</p>
  <a class="btn">Shop now!</a>
</section>

<section class="about">
  <div class="about-photo" role="img" aria-label="Marbling tray with paint jars on a workshop table"></div>
  <svg class="about-panel" width="1200" height="462" viewBox="0 0 1200 462"><polygon points="0,0 648,0 582,462 0,462" fill="#dea6c4"/></svg>
  <h2>ABOUT TA BELLE PIÈCE</h2>
  <p style="top:160px">ta belle pièce is a leading Online Store. We provide an unparalleled selection of the very best quality products, an easy and comfortable shopping experience, expedited shipping offers, and exceptional customer service. Check out our collection of new arrivals, best-sellers, and clearance items today.</p>
  <p style="top:262px">Nemo enim ipsam voluptatem quia voluptas sit aspernatur aut odit aut fugit, sed quia consequuntur magni dolores eos qui ratione voluptatem</p>
  <a class="btn">Read more ◉</a>
</section>

<section class="why">
  <h2 class="section-title" style="top:70px">WHY CHOOSE US</h2>
  <span class="rule"></span>

  <div class="feature left" style="top:190px"><h3>Quis autem vel eum</h3><p>Sed ut perspiciatis unde omnis iste natus error sit voluptatem accusantium</p></div>
  <div class="feature left" style="top:331px"><h3>Nemo enim ipsam</h3><p>Sed ut perspiciatis unde omnis iste natus error sit voluptatem accusantium</p></div>
  <div class="feature left" style="top:472px"><h3>Sed ut perspiciatis</h3><p>Sed ut perspiciatis unde omnis iste natus error sit voluptatem accusantium</p></div>
  <div class="feature right" style="top:190px"><h3>Sed ut perspiciatis</h3><p>Sed ut perspiciatis unde omnis iste natus error sit voluptatem accusantium</p></div>
  <div class="feature right" style="top:331px"><h3>Quis autem vel eum</h3><p>Sed ut perspiciatis unde omnis iste natus error sit voluptatem accusantium</p></div>
  <div class="feature right" style="top:472px"><h3>Nemo enim ipsam</h3><p>Sed ut perspiciatis unde omnis iste natus error sit voluptatem accusantium</p></div>

  <svg class="abs" style="left:0;top:0" width="1200" height="637" viewBox="0 0 1200 637">
    <defs>
      <radialGradient id="centerArt" cx="50%" cy="50%" r="50%"><stop offset="0" stop-color="#b58a84"/><stop offset="1" stop-color="#6e4a46"/></radialGradient>
    </defs>
    <g stroke="#999" stroke-width="1" fill="#777">
      <line x1="410" y1="220" x2="495" y2="220"/><circle cx="410" cy="220" r="2.5"/>
      <line x1="365" y1="377" x2="420" y2="377"/><circle cx="365" cy="377" r="2.5"/>
      <line x1="410" y1="522" x2="495" y2="522"/><circle cx="410" cy="522" r="2.5"/>
      <line x1="700" y1="220" x2="785" y2="220"/><circle cx="785" cy="220" r="2.5"/>
      <line x1="776" y1="370" x2="840" y2="370" stroke="#eeaacb"/><circle cx="840" cy="370" r="2.5"/>
      <line x1="700" y1="522" x2="785" y2="522"/><circle cx="785" cy="522" r="2.5"/>
    </g>
    <g transform="translate(598 369)" stroke="#f4f4f4" stroke-width="6">
      <path d="M0,-176 A176,176 0 0 1 152.4,-88 L85.7,-49.5 A99,99 0 0 0 0,-99Z" fill="#9a9a9a"/>
      <path d="M152.4,-88 A176,176 0 0 1 152.4,88 L85.7,49.5 A99,99 0 0 0 85.7,-49.5Z" fill="#eeaacb"/>
      <path d="M152.4,88 A176,176 0 0 1 0,176 L0,99 A99,99 0 0 0 85.7,49.5Z" fill="#eeaacb"/>
      <path d="M0,176 A176,176 0 0 1 -152.4,88 L-85.7,49.5 A99,99 0 0 0 0,99Z" fill="#9a9a9a"/>
      <path d="M-152.4,88 A176,176 0 0 1 -152.4,-88 L-85.7,-49.5 A99,99 0 0 0 -85.7,49.5Z" fill="#eeaacb"/>
      <path d="M-152.4,-88 A176,176 0 0 1 0,-176 L0,-99 A99,99 0 0 0 -85.7,-49.5Z" fill="#eeaacb"/>
    </g>
    <circle cx="598" cy="369" r="94" fill="url(#centerArt)" role="img" aria-label="Hands working on a marbling pattern"/>
    <g fill="#fff">
      <rect x="658" y="222" width="24" height="17" rx="2"/><rect x="665" y="217" width="10" height="6" fill="none" stroke="#fff" stroke-width="2"/>
      <circle cx="727" cy="369" r="9"/><circle cx="727" cy="369" r="4" fill="#eeaacb"/>
      <circle cx="667" cy="505" r="11" fill="none" stroke="#fff" stroke-width="3"/><path d="M667 499v7h5" stroke="#fff" stroke-width="2" fill="none"/>
      <rect x="517" y="496" width="22" height="17" rx="2" transform="rotate(-20 528 504)"/>
      <path d="M459 358h20v12c0 8-10 13-10 13s-10-5-10-13z"/>
      <path d="M518 242l14-18 4 4-14 18z"/><circle cx="517" cy="245" r="4"/>
    </g>
  </svg>
</section>

<section class="shop">
  <div class="shop-photo" role="img" aria-label="Marbled floral pattern on a tray with paint pots"></div>
  <div class="price">$120.00</div>
  <h2>OUR SHOP</h2>
  <p class="lead">Nemo enim ipsam voluptatem quia voluptas sit aspernatur aut odit aut fugit, sed quia consequuntur magni dolores eos qui ratione voluptatem sequi nesciunt. Neque porro quisquam est, qui dolorem ipsum quia dolor sit amet, consectetur, adipisci velit, sed quia non numquam eius modi tempora incidunt ut labore et dolore magnam aliquam quaerat voluptatem. Ut enim ad minima veniam, quis nostrum exercitationem ullam corporis suscipit laboriosam, nisi ut aliquid ex ea commodi consequatur?</p>
  <ul class="bullets">
    <li>Ut enim ad minima veniam, quis</li>
    <li>Nemo enim ipsam voluptatem quia voluptas</li>
    <li>Sed ut perspiciatis unde omnis iste</li>
    <li>Sed ut perspiciatis unde omnis iste</li>
  </ul>
  <a class="btn">Shop now!</a>
</section>

<section class="events">
  <h2 class="section-title" style="top:52px">LATEST EVENTS</h2>

  <article class="event" style="left:99px">
    <div class="event-photo" role="img" aria-label="Marbled paper held up at a class" style="background:linear-gradient(135deg,#4a3a30,#8d6a4e 50%,#b6a48a)"></div>
    <div class="date"><span class="m">APRIL</span><span class="d">02</span><span class="y">2017</span></div>
    <h3>Nemo enim ipsam voluptatem</h3>
    <div class="meta"><span class="stars">★★★<span class="off">★★</span></span><span>◯ No comments</span></div>
    <p>Sed ut perspiciatis unde omnis iste natus error sit uptatem accusantium doloremque laudantium, totam rem aperiam, eaque ipsa quae ab illo inventore veritatis</p>
  </article>

  <article class="event" style="left:444px">
    <div class="event-photo" role="img" aria-label="Workshop table with paint jars and marbling tray" style="background:linear-gradient(135deg,#2f2c2a,#5d5650 50%,#8a7f74)"></div>
    <div class="date"><span class="m">APRIL</span><span class="d">02</span><span class="y">2017</span></div>
    <h3>Nemo enim ipsam voluptatem</h3>
    <div class="meta"><span class="stars">★★★<span class="off">★★</span></span><span>◯ No comments</span></div>
    <p>Sed ut perspiciatis unde omnis iste natus error sit uptatem accusantium doloremque laudantium, totam rem aperiam, eaque ipsa quae ab illo inventore veritatis</p>
  </article>

  <article class="event" style="left:791px">
    <div class="event-photo" role="img" aria-label="Colour jars beside a marbling bath" style="background:linear-gradient(135deg,#3c4a3a,#7a5a4a 50%,#a08070)"></div>
    <div class="date"><span class="m">APRIL</span><span class="d">02</span><span class="y">2017</span></div>
    <h3>Nemo enim ipsam voluptatem</h3>
    <div class="meta"><span class="stars">★★★<span class="off">★★</span></span><span>◯ No comments</span></div>
    <p>Sed ut perspiciatis unde omnis iste natus error sit uptatem accusantium doloremque laudantium, totam rem aperiam, eaque ipsa quae ab illo inventore veritatis</p>
  </article>
</section>

<footer class="site-footer">
  <div class="footer-brand">ta belle pièce</div>
  <div class="socials"><span></span><span></span><span></span><span></span></div>

  <h4 style="left:295px">CONTACT US</h4>
  <ul class="contact">
    <li style="top:112px"><svg width="12" height="15" viewBox="0 0 12 15"><path d="M6 0a6 6 0 0 1 6 6c0 4-6 9-6 9S0 10 0 6a6 6 0 0 1 6-6z" fill="#eeaacb"/><circle cx="6" cy="6" r="2" fill="#000"/></svg>ta belle pièce<br>Lindenhofweg 27 40210 Aulendorf<br>Germany</li>
    <li style="top:184px"><svg width="14" height="14" viewBox="0 0 14 14"><path d="M3 0l3 3-2 2c1 2 3 4 5 5l2-2 3 3-2 3C6 14 0 8 0 2z" fill="#eeaacb"/></svg>Phone: +49-211-55-20-417</li>
    <li style="top:216px"><svg width="14" height="10" viewBox="0 0 14 10"><rect width="14" height="10" fill="#eeaacb"/><path d="M0 0l7 6 7-6" stroke="#000" fill="none"/></svg>Email: info@tabellepiece.com</li>
  </ul>

  <h4 style="left:622px">SIGN UP FOR NEWSLETTER</h4>
  <p class="news-text">Sed ut perspiciatis unde omnis iste natus error sit voluptatem accusantium doloremque laudantium</p>
  <div class="news-form"><div class="input">Enter Email</div><div class="submit">SUBSCRIBE</div></div>
  <div class="cards"><span></span><span></span><span></span><span></span></div>

  <h4 style="left:974px">QUICK LINKS</h4>
  <ul class="links">
    <li>Home</li><li>Products</li><li>About Us</li><li>My blog</li><li>Shop</li><li>Contacts</li><li>Book</li>
  </ul>
</footer>
<div class="bottom-bar">©2017 ta belle pièce. All Rights Reserved.</div>

</body>
</html>
```